Simple and clean

We need a business card design for a new company called Dwelling Owl. It is a search engine to find current properties for sale or rent in New Zealand market.
We have already a colour scheme that we would like people to use.
Light brown: #D4CCB0
Light green: #D6E4D4
Green: #669966
Black/White
It is OK to divert from this colour scheme slightly as long as there is a green component to the business card.
Final design should be clean, simple and should communicate the nature of the business.
Target Market(s)
- First home buyers
- Real estate agents
- People seeking rentals
Industry/Entity Type
Business
Requirements
Must have
- Use those or similar colours.
Light brown: #D4CCB0
Light green: #D6E4D4
Green: #669966
Black/White

```html
<!DOCTYPE html>
<html lang="en">
<head>
<meta charset="utf-8">
<title>Dwelling Owl – Business Card</title>
<link rel="stylesheet" href="https://fonts.googleapis.com/css2?family=Arimo:ital,wght@0,400;0,700;1,400&display=swap">
<style>
  :root {
    --light-green: #d6e4d4;
    --white: #ffffff;
    --ink: #1c1c1c;
    --label-grey: #8a8f8a;
    --value-grey: #4a4d4a;
    --title-green: #8fb08f;
    --divider: rgba(255, 255, 255, 0.55);
  }
  html, body {
    margin: 0;
    padding: 0;
    width: 1200px;
    height: 690px;
    overflow: hidden;
    background: var(--white);
  }
  .card {
    position: relative;
    width: 1200px;
    height: 690px;
    overflow: hidden;
    font-family: "Arimo", Arial, sans-serif;
    background: linear-gradient(90deg,
      var(--light-green) 0%,
      var(--light-green) 56%,
      #e6efe5 70%,
      #f6f9f5 82%,
      var(--white) 92%);
  }
  .brand {
    position: absolute;
    left: 862px;
    top: 68px;
    display: flex;
    align-items: center;
    gap: 14px;
  }
  .brand__dot {
    width: 86px;
    height: 86px;
    border-radius: 50%;
    background: var(--white);
  }
  .brand__name {
    font-size: 31px;
    font-weight: 700;
    color: var(--ink);
    letter-spacing: -0.3px;
  }
  .person {
    position: absolute;
    right: 677px;
    top: 296px;
    text-align: right;
  }
  .person__name {
    margin: 0;
    font-size: 29px;
    font-weight: 700;
    color: var(--ink);
    line-height: 1;
  }
  .person__role {
    margin: 8px 0 0;
    font-size: 21px;
    font-style: italic;
    color: var(--title-green);
    line-height: 1;
  }
  .divider {
    position: absolute;
    left: 545px;
    top: 173px;
    width: 1px;
    height: 352px;
    background: var(--divider);
  }
  .contact {
    position: absolute;
    left: 567px;
    top: 302px;
    margin: 0;
    padding: 0;
    list-style: none;
    font-size: 21px;
    line-height: 27.5px;
  }
  .contact__label { color: var(--label-grey); }
  .contact__value { color: var(--value-grey); }
</style>
</head>
<body>
  <main class="card">
    <div class="brand">
      <span class="brand__dot" aria-hidden="true"></span>
      <span class="brand__name">Dwelling Owl</span>
    </div>

    <div class="person">
      <p class="person__name">Tom Harlow</p>
      <p class="person__role">Director</p>
    </div>

    <div class="divider" aria-hidden="true"></div>

    <ul class="contact">
      <li><span class="contact__label">Web: </span><span class="contact__value">www.dwellingowl.co.nz</span></li>
      <li><span class="contact__label">Mobil: </span><span class="contact__value">xx xxxxxx xxx</span></li>
      <li><span class="contact__label">E-mail: </span><span class="contact__value">hello@dwellingowl.co.nz</span></li>
    </ul>
  </main>
</body>
</html>
```